Kestrel Photography Business Card

I need a business card designed for a photography business based in Perth, Western Australia called Kestrel Photography.

We specialise in wedding, event photography and portrait photography.

The business card must borrow the style of the attached logo.

The hex codes for the colours in the logo are:
#ED1D85 - Pink
#89C23E - Green
#37282F - Black

The name on the card will be:
Name: Toviran
Phone: 0417395268
Website: www.kestrelphotography.com.au
Facebook: kestrelphotography

I am open and happy to accept creative concepts.

I’d like some space at the back for writing notes and appointment details.

```html
<!DOCTYPE html>
<html lang="en">
<head>
<meta charset="utf-8">
<title>Kestrel Photography – Business Card</title>
<link rel="stylesheet" href="https://fonts.googleapis.com/css2?family=Cabin:ital,wght@0,400;0,600;1,700&family=Raleway:wght@300&display=swap">
<style>
  :root {
    --pink: #ED1D85;
    --green: #89C23E;
    --black: #37282F;
    --ink: #2f2a2d;
    --silver-light: #ffffff;
    --silver-mid: #e4e4e6;
    --silver-dark: #b9b9bd;
    --backdrop: #efece8;
  }
  * { box-sizing: border-box; margin: 0; padding: 0; }
  html, body { width: 1200px; height: 565px; overflow: hidden; }
  body {
    background: var(--backdrop);
    font-family: "Cabin", Arial, sans-serif;
    display: flex;
    align-items: center;
    justify-content: center;
    gap: 60px;
  }
  .card {
    position: relative;
    width: 500px;
    height: 286px;
    border-radius: 22px;
    overflow: hidden;
    background: radial-gradient(ellipse at 45% 50%, var(--silver-light) 0%, var(--silver-mid) 60%, var(--silver-dark) 100%);
    box-shadow: 0 6px 14px rgba(0,0,0,0.18);
  }
  /* Front */
  .petal-field {
    position: absolute;
    inset: 0;
    background:
      radial-gradient(circle at 50% 50%, transparent 0 90px, rgba(137,194,62,0.22) 110px, rgba(137,194,62,0.10) 160px, rgba(237,29,133,0.22) 200px, rgba(237,29,133,0.30) 260px, transparent 320px);
  }
  .front-mark {
    position: absolute;
    left: 50%; top: 50%;
    transform: translate(-50%, -50%);
    display: flex; flex-direction: column; align-items: center; gap: 12px;
  }
  .mark-dot {
    width: 96px; height: 96px;
    border-radius: 50%;
    background: var(--pink);
  }
  .mark-name {
    font-weight: 600;
    font-size: 18px;
    letter-spacing: 1px;
    color: var(--pink);
  }
  /* Back */
  .back-heading {
    position: absolute;
    left: 30px; top: 28px;
    font-family: "Raleway", Arial, sans-serif;
    font-weight: 300;
    font-size: 15px;
    letter-spacing: 8.5px;
    color: var(--ink);
    white-space: nowrap;
  }
  .back-mark {
    position: absolute;
    right: 10px; top: 38px;
    width: 230px; height: 230px;
    display: flex; align-items: center; justify-content: center;
  }
  .back-mark-circle {
    position: absolute; inset: 0;
    border-radius: 50%;
    background: radial-gradient(circle, rgba(137,194,62,0.18) 0 45%, rgba(237,29,133,0.18) 60%, transparent 72%);
  }
  .back-mark-name {
    position: relative;
    font-weight: 600;
    font-size: 16px;
    color: rgba(55,40,47,0.18);
  }
  .contact {
    position: absolute;
    left: 30px; bottom: 24px;
    color: var(--ink);
    font-size: 15px;
    line-height: 1.45;
  }
  .contact-name {
    font-style: italic;
    font-weight: 700;
    font-size: 19px;
    color: var(--pink);
    margin-bottom: 2px;
  }
</style>
</head>
<body>
  <section class="card card-front" aria-label="Card front">
    <div class="petal-field" role="img" aria-label="Soft pink and green petal pattern radiating from the centre"></div>
    <div class="front-mark">
      <span class="mark-dot"></span>
      <span class="mark-name">Kestrel Photography</span>
    </div>
  </section>

  <section class="card card-back" aria-label="Card back">
    <h1 class="back-heading">KESTREL PHOTOGRAPHY</h1>
    <div class="back-mark" role="img" aria-label="Faint brand mark watermark">
      <span class="back-mark-circle"></span>
      <span class="back-mark-name">Kestrel Photography</span>
    </div>
    <div class="contact">
      <p class="contact-name">Toviran</p>
      <p>Phone: 0417 395 268</p>
      <p>www.kestrelphotography.com.au</p>
      <p>facebook.com/KestrelPhotography</p>
    </div>
  </section>
</body>
</html>
```